Counsel Atelier

we need all the matirials for the office to speak with the internet site
www.cunatel.example

look stilish and modern yet very respecteble

our logo needs to be our logo and some times

just the letters " Cunatel " done nicely.

We need to send e mails with a design

Firm paper

and our gmail products to look nice when we use google docs

so we need a place for

lawers names and

the cunatel

and logo

and address

and some one to help us do it all

Target Market(s)

Big firms

Industry/Entity Type

Law Firm

Font styles to use
Serif

Requirements
Must have
• Rememrable
• Different yet respectable
• For multi languages
• LAW
• B
• LAWYERS
• BOUTIQUE
Nice to have
• Clean Design
• impressive
• i put on a new card i liked
• We should not put any decorations and beautiful logo
• it's against the law for lawyers
• I have a card that proves that we are smart and boutiques
• This card that I attached as an example
• Makes you little work, and certainly - apart from everyone
• Would love this design idea
• The numbers stated hiding it from top to bottom
• I put my real information integration profile
• The thing is that people should enlighten other options and other card
• This should be accessible designer fee changes
• Still very respectable and serious
• it needs to say among other creative stuff
• Counsel atelier CUNATEL
• TOMAS VELLINGRO
• 052-7164291
• 1@cunatel.example
• www.cunatel.example
• but any smart idea
Should not have
• We have a problam
• It turns out that the law of the Bar Association in
• Our country
• Do not allow to put the firm logo on business cards
• Or office paper
• the logo can only be letters and names
• So we should convey the idea of all sorts of areas along
• As we tried with our logo
• Through the letters themselves
• And their integration with each other

```html
<!DOCTYPE html>
<html lang="en">
<head>
<meta charset="utf-8">
<title>Counsel Atelier — Business Card</title>
<link href="https://fonts.googleapis.com/css2?family=Roboto+Condensed:wght@700&family=Montserrat:wght@400;500&display=swap" rel="stylesheet">
<style>
  :root {
    --backdrop: #1d1d1d;
    --card-light: #f4f4f4;
    --card-dark: #2a2a2a;
    --band: #7d7d7d;
    --ink: #2b2b2b;
    --ink-soft: #3a3a3a;
    --muted: #7a7a7a;
    --rule: #6f6f6f;
    --paper-text: #f2f2f2;
  }
  * { margin: 0; padding: 0; box-sizing: border-box; }
  html, body {
    width: 1200px; height: 900px; overflow: hidden;
    background: var(--backdrop);
  }
  .canvas { position: relative; width: 1200px; height: 900px; }
  .card {
    position: absolute; left: 354px; width: 488px; height: 279px;
    box-shadow: 0 6px 18px rgba(0,0,0,0.45);
  }
  .card--front { top: 153px; background: var(--card-light); overflow: hidden; }
  .card--back { top: 464px; background: var(--card-dark); }

  .wordmark {
    font-family: "Roboto Condensed", "Arial Narrow", sans-serif;
    font-weight: 700; letter-spacing: -0.5px; line-height: 1;
  }
  .front-brand { position: absolute; left: 68px; top: 103px; }
  .front-brand .wordmark { font-size: 46px; color: var(--ink); }
  .front-brand .tagline {
    font-family: "Roboto Condensed", "Arial Narrow", sans-serif;
    font-weight: 700; font-size: 15.5px; color: var(--muted); margin-top: 6px;
  }

  .rule { position: absolute; left: 244px; width: 2px; background: var(--rule); }
  .rule--name { top: 61px; height: 39px; }
  .rule--contact { top: 120px; height: 105px; }

  .details {
    position: absolute; left: 264px;
    font-family: "Montserrat", Arial, sans-serif; color: var(--ink-soft);
  }
  .person { top: 62px; }
  .person .name { font-size: 17px; font-weight: 500; color: var(--ink); line-height: 1.2; }
  .person .role { font-size: 13px; line-height: 1.4; }
  .contact { top: 124px; font-size: 13px; line-height: 16.5px; }
  .contact .address { margin-bottom: 6px; }
  .contact-row { display: flex; align-items: center; }
  .contact-row svg { width: 10px; height: 10px; margin-right: 9px; fill: var(--muted); }

  .band { position: absolute; left: 0; bottom: 0; width: 100%; height: 16px; background: var(--band); }

  .back-brand { position: absolute; left: 0; right: 0; top: 106px; text-align: center; color: var(--paper-text); }
  .back-brand .wordmark { font-size: 62px; }
  .back-brand .tagline {
    font-family: "Roboto Condensed", "Arial Narrow", sans-serif;
    font-weight: 700; font-size: 19px; margin-top: 8px;
  }
</style>
</head>
<body>
<main class="canvas">
  <section class="card card--front">
    <div class="front-brand">
      <div class="wordmark">Cunatel</div>
      <div class="tagline">Counsel atelier</div>
    </div>

    <span class="rule rule--name"></span>
    <div class="details person">
      <div class="name">Tomas Vellingro</div>
      <div class="role">President &amp; CEO</div>
    </div>

    <span class="rule rule--contact"></span>
    <div class="details contact">
      <div class="address">418 Brennick Avenue<br>New York, NY 10031</div>
      <div class="contact-row">
        <svg viewBox="0 0 10 10"><path d="M2 0.5 L3.6 2.6 L2.8 3.6 C3.4 5 4.8 6.4 6.3 7.1 L7.3 6.3 L9.5 7.9 L8.4 9.5 C4.5 9.2 0.8 5.5 0.5 1.6 Z"/></svg>
        <span>052-7164291</span>
      </div>
      <div class="contact-row">
        <svg viewBox="0 0 10 10"><path d="M0.5 2 H9.5 V8.5 H0.5 Z M0.5 2 L5 5.4 L9.5 2" /><path d="M1 2.4 L5 5.4 L9 2.4" fill="#f4f4f4"/></svg>
        <span>1@cunatel.example</span>
      </div>
      <div class="contact-row">
        <svg viewBox="0 0 10 10"><circle cx="5" cy="5" r="4.6"/><path d="M2 3.5 H8 M1.2 6 H8.8 M5 0.6 C3 3 3 7 5 9.4 M5 0.6 C7 3 7 7 5 9.4" stroke="#f4f4f4" stroke-width="0.7" fill="none"/></svg>
        <span>www.cunatel.example</span>
      </div>
    </div>

    <div class="band"></div>
  </section>

  <section class="card card--back">
    <div class="back-brand">
      <div class="wordmark">Cunatel</div>
      <div class="tagline">Counsel atelier</div>
    </div>
  </section>
</main>
</body>
</html>
```